continuing medical education travel company. luxury, professional, quality service

PLEASE USE THE REVISED LOGO FOR ALL CARD DESIGNS, NO SNAKE HEAD

Target Market(s)

physicians

Industry/Entity Type

Travel Industry

Contact Information for Business Card

luxury quality, spot uv, foil, rounded corners

Colors
0255a3
3176b5
cfdeed
aaaaaa
5c5c5c

Requirements
Must have
• navy, platinum, possible holographic

```html
<!DOCTYPE html>
<html lang="en">
<head>
<meta charset="utf-8">
<title>Veralo Travel — Business Cards</title>
<link rel="stylesheet" href="https://fonts.googleapis.com/css2?family=Damion&family=Montserrat:wght@600;700&display=swap">
<style>
  :root {
    --backdrop: #f4f2f6;
    --metal-light: #76848b;
    --metal-mid: #65737a;
    --metal-dark: #56646b;
    --ink: #0d1a22;
    --ink-soft: #1b2a33;
    --edge-glow: #cfe6ee;
    --navy: #0255a3;
  }
  * { box-sizing: border-box; margin: 0; padding: 0; }
  html, body {
    width: 1200px; height: 960px; overflow: hidden;
    background: var(--backdrop);
  }
  .canvas { position: relative; width: 1200px; height: 960px; }

  .card {
    position: absolute;
    width: 560px; height: 320px;
    border-radius: 22px;
    background:
      repeating-linear-gradient(180deg, rgba(255,255,255,0.05) 0 1px, rgba(0,0,0,0.04) 1px 3px),
      linear-gradient(160deg, var(--metal-light), var(--metal-mid) 50%, var(--metal-dark));
    box-shadow: 0 6px 18px rgba(40,50,60,0.25);
    overflow: hidden;
  }
  .card--info { left: 60px; top: 130px; }
  .card--brand { left: 580px; top: 510px; }

  /* Info side */
  .holder {
    position: absolute; right: 44px; top: 34px;
    text-align: right;
    font-family: "Damion", cursive;
    color: var(--ink);
    text-shadow: 0 1px 0 var(--edge-glow);
    line-height: 1;
  }
  .holder__name { font-size: 40px; }
  .holder__title { font-size: 34px; margin-top: 2px; }

  .contact-list {
    position: absolute; left: 30px; top: 138px;
    list-style: none;
    font-family: "Montserrat", sans-serif;
    font-weight: 700; font-size: 16px;
    color: var(--ink-soft);
    text-shadow: 0 1px 0 var(--edge-glow);
  }
  .contact-list li {
    display: flex; align-items: center; gap: 16px;
    min-height: 40px; margin-bottom: 6px;
  }
  .contact-list svg { width: 32px; height: 32px; flex: none; }
  .contact-list .address { line-height: 1.3; }

  .brand-mini {
    position: absolute; right: 40px; bottom: 48px;
    font-family: "Montserrat", sans-serif;
    font-weight: 700; font-size: 22px;
    color: var(--ink);
    display: flex; align-items: center; gap: 10px;
  }
  .brand-mini .mark { width: 14px; height: 14px; border-radius: 50%; background: var(--ink); }

  /* Brand side */
  .brand-main {
    position: absolute; inset: 0;
    display: flex; align-items: center; justify-content: center; gap: 18px;
    font-family: "Montserrat", sans-serif;
    font-weight: 700; font-size: 50px;
    color: var(--ink);
  }
  .brand-main .mark { width: 30px; height: 30px; border-radius: 50%; background: var(--ink); }
</style>
</head>
<body>
<main class="canvas">

  <section class="card card--info" aria-label="Business card, contact side">
    <div class="holder">
      <div class="holder__name">Nora Whitfield</div>
      <div class="holder__title">Principal</div>
    </div>

    <ul class="contact-list">
      <li>
        <svg viewBox="0 0 32 32" aria-hidden="true"><circle cx="16" cy="16" r="13" fill="none" stroke="#0d1a22" stroke-width="2"/><path d="M11 9c-1 1-1.5 3 0 6s4 6 7 7.5 4 .5 5-.5l-3-3-2 1c-1-.5-3-2.5-3.5-3.5l1-2z" fill="#0d1a22"/></svg>
        <span>555.014.2290</span>
      </li>
      <li>
        <svg viewBox="0 0 32 32" aria-hidden="true"><rect x="4" y="8" width="24" height="17" rx="1.5" fill="none" stroke="#0d1a22" stroke-width="2"/><path d="M4 9l12 9 12-9" fill="none" stroke="#0d1a22" stroke-width="2"/></svg>
        <span>nwhitfield@veralotravel.com</span>
      </li>
      <li>
        <svg viewBox="0 0 32 32" aria-hidden="true"><path d="M16 4a7 7 0 0 0-7 7c0 5 7 12 7 12s7-7 7-12a7 7 0 0 0-7-7z" fill="none" stroke="#0d1a22" stroke-width="2"/><circle cx="16" cy="11" r="2.5" fill="#0d1a22"/><path d="M5 24h22v4H5z" fill="#0d1a22"/></svg>
        <span class="address">18 Maple Row, Lakeside,<br>QC H0H 0A1</span>
      </li>
      <li>
        <svg viewBox="0 0 32 32" aria-hidden="true"><circle cx="16" cy="16" r="12" fill="none" stroke="#0d1a22" stroke-width="2"/><ellipse cx="16" cy="16" rx="5" ry="12" fill="none" stroke="#0d1a22" stroke-width="1.6"/><path d="M4 16h24M6 10h20M6 22h20" stroke="#0d1a22" stroke-width="1.6"/></svg>
        <span>VERALOTRAVEL.COM</span>
      </li>
    </ul>

    <div class="brand-mini"><span class="mark"></span>Veralo Travel</div>
  </section>

  <section class="card card--brand" aria-label="Business card, brand side">
    <div class="brand-main"><span class="mark"></span>Veralo Travel</div>
  </section>

</main>
</body>
</html>
```